Rig up a website for a Rigging Company

We already have a logo. Looking for a website design that works on pagebarn.com.
Our rigging company uses semi trucks, forklifts, and similar equipment to move large machines.
Our logo is white, black and red.

Target Market(s)

Medical Industry (moving medical equipment), Utility Industry (power equipment), Food Industry (moving bottling/packing equipment), US Government (large equipment)

Industry/Entity Type

It Company

Coding

Coded - Design and coding required

Number of Pages Required

5+ page

Font styles to use
Sans Serif

Colors
ec1f27
ffffff
0355a3

Requirements
Must have
• Home page, About page, Services Page, and Contact Information page
Nice to have
• Pictures of semi and forklifts and ability to insert our own pictures of our equipment

```html
<!DOCTYPE html>
<html lang="en">
<head>
<meta charset="utf-8">
<title>Holt Rigging</title>
<link href="https://fonts.googleapis.com/css2?family=Open+Sans:wght@400;600;700&family=Roboto:wght@400;500;700&family=Exo+2:wght@700&display=swap" rel="stylesheet">
<style>
:root{
  --red:#e8232b;
  --dark:#222;
  --text:#333;
  --muted:#555;
  --grey-bg:#f0f0f0;
  --ring:#5a5a5a;
  --white:#fff;
  --footer-bar:#e6e6e6;
}
*{box-sizing:border-box;margin:0;padding:0}
html,body{width:1200px;height:2875px;overflow:hidden}
body{position:relative;background:var(--white);font-family:"Open Sans",Arial,sans-serif;color:var(--text)}
.abs{position:absolute}
a{color:inherit;text-decoration:none}

/* header */
.site-header{position:absolute;left:0;top:0;width:1200px;height:143px;border-top:4px solid var(--red);background:var(--white)}
.brand{position:absolute;left:100px;top:52px;display:flex;align-items:center;gap:10px;font-family:"Roboto",sans-serif;font-weight:700;font-size:34px;color:var(--dark);letter-spacing:-0.5px}
.brand-mark{width:18px;height:18px;background:var(--red)}
.top-contact{position:absolute;top:28px;left:556px;display:flex;align-items:center;gap:10px;font-size:16px;font-weight:600}
.icon-disc{width:34px;height:34px;border-radius:50%;display:flex;align-items:center;justify-content:center}
.icon-disc.red{background:var(--red)}
.icon-disc.dark{background:#333}
.top-contact .email{color:var(--red);margin-right:24px}
.socials{position:absolute;top:33px;left:960px;display:flex;gap:6px}
.socials span{width:22px;height:22px;background:#3b8fd0}
.socials span:nth-child(2){background:#1b74b4}
.socials span:nth-child(3){background:#888}
.socials span:nth-child(4){background:#3b5a98}
.socials span:nth-child(5){background:#cc2020}
.main-nav{position:absolute;top:98px;left:449px;display:flex;gap:0;font-family:"Roboto",sans-serif;font-size:14px;font-weight:500;color:var(--dark)}
.main-nav a{margin-right:48px}
.main-nav a:last-child{margin-right:0}
.main-nav .active{color:var(--red)}

/* hero */
.hero{position:absolute;left:0;top:143px;width:1200px;height:500px;background:linear-gradient(180deg,#5d6e86 0%,#4a5568 35%,#6b5a4e 70%,#8a6a52 100%)}
.hero-curve{position:absolute;left:0;top:560px;width:1200px;height:90px}
.hero-title{position:absolute;top:265px;width:1200px;text-align:center;font-family:"Exo 2",sans-serif;font-weight:700;font-size:58px;color:var(--white);letter-spacing:1px}
.hero-lead{position:absolute;top:362px;left:225px;width:750px;text-align:center;color:var(--white);font-size:15px;font-weight:600;line-height:29px}
.hero-arrow{position:absolute;top:350px}

/* feature circles */
.feature{position:absolute;width:340px;text-align:center}
.feature .hook{display:block;margin:0 auto}
.feature .photo{width:246px;height:246px;border-radius:50%;border:12px solid var(--ring);margin:6px auto 0}
.feature .photo.hot{border-color:var(--red)}
.feature h3{margin-top:22px;font-family:"Roboto",sans-serif;font-size:20px;font-weight:500;color:var(--red)}
.feature p{margin:14px auto 0;width:290px;font-size:13.5px;line-height:21px;color:var(--text)}
.read-link{display:inline-block;margin-top:18px;color:var(--red);font-family:"Roboto",sans-serif;font-weight:700;font-size:14px}

/* about */
.about{position:absolute;left:0;top:1010px;width:1200px;height:410px;background:var(--grey-bg)}
.section-title{font-family:"Roboto",sans-serif;font-weight:500;font-size:26px;color:var(--red)}
.rule{height:2px;background:var(--red);width:170px}
.about .section-title{position:absolute;left:99px;top:45px}
.about .rule{position:absolute;left:99px;top:88px}
.about p{position:absolute;left:99px;width:585px;font-size:12.5px;line-height:23px;color:var(--text)}
.btn{position:absolute;display:flex;align-items:center;justify-content:center;font-family:"Roboto",sans-serif;font-size:14px;font-weight:500;border-radius:3px}
.btn.solid{background:var(--red);color:var(--white)}
.btn.line{border:2px solid var(--dark);color:var(--dark);background:var(--white)}
.about-photo{position:absolute;left:721px;top:58px;width:377px;height:285px;border:3px solid #d5d5d5;background:linear-gradient(160deg,#3f86d4 0%,#7fb4e6 45%,#c9b77b 80%,#5b5040 100%)}

/* services */
.services .section-title{position:absolute;top:1470px;width:1200px;text-align:center}
.services .rule{position:absolute;top:1517px;left:554px;width:92px}
.service{position:absolute;top:1558px;width:316px;text-align:center}
.service .photo{height:229px}
.service h4{margin-top:30px;font-family:"Roboto",sans-serif;font-weight:500;font-size:18px;color:var(--dark)}
.service p{margin-top:14px;font-size:12px;line-height:20px;color:var(--muted)}
.service .btn{position:relative;margin:30px auto 0;width:124px;height:44px;font-size:13px}

/* testimonials */
.testimonials{position:absolute;left:0;top:2047px;width:1200px;height:430px;background:var(--grey-bg)}
.testimonials .section-title{position:absolute;top:55px;width:1200px;text-align:center}
.testimonials .rule{position:absolute;top:102px;left:554px;width:92px}
.review{position:absolute;top:180px;width:520px}
.avatar{position:absolute;left:30px;top:0;width:104px;height:104px;border-radius:50%;border:3px solid var(--white);box-shadow:0 0 0 3px #2b4a6e;background:linear-gradient(160deg,#e8d6c0,#c9a987)}
.quote{position:absolute;left:170px;top:-6px}
.review h5{position:absolute;left:206px;top:20px;font-family:"Roboto",sans-serif;font-weight:500;font-size:17px;color:var(--dark)}
.review .who{position:absolute;left:206px;top:52px;font-size:15px;color:var(--muted)}
.stars{position:absolute;left:206px;top:82px;display:flex;gap:3px}
.review p{position:absolute;left:0;top:190px;width:520px;font-size:12px;line-height:21px;color:var(--muted)}

/* footer */
.site-footer{position:absolute;left:0;top:2477px;width:1200px;height:337px;border-top:4px solid var(--red);background:linear-gradient(180deg,#f6f6f4,#ececea)}
.footer-brand{position:absolute;left:100px;top:170px}
.footer-col{position:absolute;top:50px}
.footer-col h6{font-family:"Roboto",sans-serif;font-weight:500;font-size:17px;color:var(--red)}
.footer-col .rule{width:100px;margin-top:12px}
.quick-links{list-style:none;margin-top:20px;font-size:14px;color:var(--dark)}
.quick-links li{height:31.5px}
.contact-item{display:flex;gap:14px;margin-top:22px}
.contact-item .ring{width:38px;height:38px;border-radius:50%;border:2px solid var(--red);flex:none;display:flex;align-items:center;justify-content:center}
.contact-item b{display:block;font-family:"Roboto",sans-serif;font-weight:700;font-size:14px;color:var(--dark)}
.contact-item span{font-size:12.5px;line-height:19px;color:var(--muted)}
.contact-form{position:relative;margin-top:22px;width:286px}
.field{position:absolute;background:var(--white);border:1px solid #aaa;border-radius:2px;font-size:11px;color:var(--dark);padding:8px 10px}
.send{position:absolute;left:0;top:178px;width:120px;height:38px;background:var(--red);color:var(--white);font-family:"Roboto",sans-serif;font-size:12px;font-weight:500;display:flex;align-items:center;justify-content:center;border-radius:2px}
.footer-bar{position:absolute;left:0;top:2814px;width:1200px;height:61px;background:var(--footer-bar)}
.footer-bar .copy{position:absolute;left:100px;top:20px;font-size:14px;color:var(--dark)}
.footer-social{position:absolute;left:898px;top:14px;display:flex;gap:10px}
.footer-social span{width:32px;height:32px;border-radius:50%;border:2px solid #333}
</style>
</head>
<body>

<header class="site-header">
  <div class="brand"><span class="brand-mark"></span>Holt Rigging</div>
  <div class="top-contact">
    <span class="icon-disc red"><svg width="16" height="12" viewBox="0 0 16 12"><rect x="0.5" y="0.5" width="15" height="11" fill="none" stroke="#fff"/><path d="M1 1l7 6 7-6" fill="none" stroke="#fff"/></svg></span>
    <a class="email">info@holtrigging.com</a>
    <span class="icon-disc dark"><svg width="14" height="14" viewBox="0 0 24 24"><path fill="#fff" d="M6.6 10.8a15 15 0 006.6 6.6l2.2-2.2c.3-.3.7-.4 1-.2 1.1.4 2.3.6 3.6.6.6 0 1 .4 1 1V20c0 .6-.4 1-1 1A17 17 0 013 4c0-.6.4-1 1-1h3.5c.6 0 1 .4 1 1 0 1.3.2 2.5.6 3.6.1.3 0 .7-.2 1z"/></svg></span>
    <span>180 555 0142</span>
  </div>
  <div class="socials"><span></span><span></span><span></span><span></span><span></span></div>
  <nav class="main-nav">
    <a class="active">HOME</a><a>SERVICES</a><a>GALLERY</a><a>RIGGING</a><a>TESTIMONIALS</a><a>CONTACT US</a>
  </nav>
</header>

<section class="hero" role="img" aria-label="Container port with cranes and stacked shipping containers at dusk"></section>
<svg class="hero-curve" viewBox="0 0 1200 90" preserveAspectRatio="none"><path d="M0 0 Q600 80 1200 0 L1200 90 L0 90z" fill="#fff"/></svg>
<h1 class="hero-title">HOLT RIGGING</h1>
<p class="hero-lead">We are a rigging company. Our rigging company uses semi trucks, forklifts, and similar equipment to move large machines.</p>
<svg class="hero-arrow" style="left:32px" width="30" height="54" viewBox="0 0 30 54"><path d="M27 2L3 27l24 25" fill="none" stroke="#fff" stroke-width="2"/></svg>
<svg class="hero-arrow" style="left:1138px" width="30" height="54" viewBox="0 0 30 54"><path d="M3 2l24 25L3 52" fill="none" stroke="#fff" stroke-width="2"/></svg>

<div class="feature" style="left:75px;top:508px">
  <svg class="hook" width="44" height="68" viewBox="0 0 44 68"><rect x="14" y="2" width="16" height="14" rx="3" fill="none" stroke="#fff" stroke-width="4"/><path d="M22 16v14M22 30c-12 0-16 10-12 18 5 9 20 9 24-1" fill="none" stroke="#fff" stroke-width="5" stroke-linecap="round"/></svg>
  <div class="photo" role="img" aria-label="Red semi truck on a road" style="background:linear-gradient(160deg,#6f8fb8,#9a6a5a 55%,#5a5a5a)"></div>
  <h3>SEMI TRUCKS</h3>
  <p>Nemo enim ipsam voluptatem quia voluptas sit aspernatur aut odit aut fugit, sed quia consequuntur magni dolores.</p>
  <a class="read-link">READ MORE &nbsp;➜</a>
</div>
<div class="feature" style="left:436px;top:508px">
  <svg class="hook" width="44" height="68" viewBox="0 0 44 68"><rect x="14" y="2" width="16" height="14" rx="3" fill="none" stroke="#fff" stroke-width="4"/><path d="M22 16v14M22 30c-12 0-16 10-12 18 5 9 20 9 24-1" fill="none" stroke="#fff" stroke-width="5" stroke-linecap="round"/></svg>
  <div class="photo hot" role="img" aria-label="Forklift lifting stacked shipping containers" style="background:linear-gradient(160deg,#4d8ad0,#5c7fa8 50%,#c0a040)"></div>
  <h3>FORKLIFTS</h3>
  <p>Nemo enim ipsam voluptatem quia voluptas sit aspernatur aut odit aut fugit, sed quia consequuntur magni dolores.</p>
  <a class="read-link">READ MORE &nbsp;➜</a>
</div>
<div class="feature" style="left:783px;top:508px">
  <svg class="hook" width="44" height="68" viewBox="0 0 44 68"><rect x="14" y="2" width="16" height="14" rx="3" fill="none" stroke="#fff" stroke-width="4"/><path d="M22 16v14M22 30c-12 0-16 10-12 18 5 9 20 9 24-1" fill="none" stroke="#fff" stroke-width="5" stroke-linecap="round"/></svg>
  <div class="photo" role="img" aria-label="Warehouse worker operating a pallet stacker between shelves" style="background:linear-gradient(160deg,#b8a890,#8a7a6a 55%,#d08a3a)"></div>
  <h3>LARGE MACHINES</h3>
  <p>Nemo enim ipsam voluptatem quia voluptas sit aspernatur aut odit aut fugit, sed quia consequuntur magni dolores.</p>
  <a class="read-link">READ MORE &nbsp;➜</a>
</div>

<section class="about">
  <h2 class="section-title">About Holt Rigging</h2>
  <div class="rule"></div>
  <p style="top:112px">Nemo enim ipsam voluptatem quia voluptas sit aspernatur aut odit aut fugit, sed quia consequuntur magni dolores eos qui ratione voluptatem sequi nesciunt. Neque porro quisquam est, qui dolorem ipsum quia dolor sit amet, consectetur, adipisci velit.</p>
  <p style="top:200px">Sed ut perspiciatis unde omnis iste natus error sit voluptatem accusantium doloremque laudantium, totam rem aperiam, eaque ipsa quae ab illo inventore veritatis et quasi architecto beatae vitae dicta sunt explicabo.</p>
  <a class="btn solid" style="left:99px;top:300px;width:110px;height:42px">Read More</a>
  <a class="btn line" style="left:222px;top:300px;width:110px;height:42px">Contact Us</a>
  <div class="about-photo" role="img" aria-label="Mobile crane lifting a large unit against a blue sky"></div>
</section>

<section class="services">
  <h2 class="section-title">Our Services</h2>
  <div class="rule"></div>
  <div class="service" style="left:100px">
    <div class="photo" role="img" aria-label="Row of trucks parked at a depot under a sunset sky" style="background:linear-gradient(180deg,#6e7f9c,#b27c6a 50%,#7a7a7a)"></div>
    <h4>Rigging Service</h4>
    <p>Nemo enim ipsam voluptatem quia voluptas sit asper natur aut odit aut fugit, sed quia consequuntur magni dolores eos qui ratione voluptatem.</p>
    <a class="btn solid">READ MORE</a>
  </div>
  <div class="service" style="left:443px">
    <div class="photo" role="img" aria-label="Orange forklift moving cardboard boxes in a warehouse" style="background:linear-gradient(160deg,#e8dcc8,#c9a778 50%,#9a9a9a)"></div>
    <h4>Holt Rigging</h4>
    <p>Nemo enim ipsam voluptatem quia voluptas sit asper natur aut odit aut fugit, sed quia consequuntur magni dolores eos qui ratione voluptatem.</p>
    <a class="btn line">READ MORE</a>
  </div>
  <div class="service" style="left:784px">
    <div class="photo" role="img" aria-label="Container yard with stacked containers at sunset" style="background:linear-gradient(160deg,#5a6a7a,#e09a40 55%,#7a4a2a)"></div>
    <h4>Large Machines</h4>
    <p>Nemo enim ipsam voluptatem quia voluptas sit asper natur aut odit aut fugit, sed quia consequuntur magni dolores eos qui ratione voluptatem.</p>
    <a class="btn line">READ MORE</a>
  </div>
</section>

<section class="testimonials">
  <h2 class="section-title">Our Testimonials</h2>
  <div class="rule"></div>
  <div class="review" style="left:100px">
    <div class="avatar" role="img" aria-label="Customer portrait"></div>
    <svg class="quote" width="30" height="24" viewBox="0 0 30 24"><path d="M0 0h12v12L6 24H2l4-12H0zM16 0h12v12l-6 12h-4l4-12h-6z" fill="#e8232b"/></svg>
    <h5>GOOD SERVICE</h5>
    <span class="who">Marissa</span>
    <div class="stars">
      <svg width="80" height="14" viewBox="0 0 80 14"><g fill="#e8232b"><path id="s" d="M7 0l2 4.6 5 .4-3.8 3.2 1.2 4.8L7 10.4 2.6 13l1.2-4.8L0 5l5-.4z"/><use href="#s" x="16"/><use href="#s" x="32"/><use href="#s" x="48"/></g><use href="#s" x="64" fill="none" stroke="#e8232b"/></svg>
    </div>
    <p>Neque porro quisquam est, qui dolorem ipsum quia dolor sit amet, consectetur, adipisci velit, sed quia non numquam eius modi tempora.</p>
  </div>
  <div class="review" style="left:640px">
    <div class="avatar" role="img" aria-label="Customer portrait"></div>
    <svg class="quote" width="30" height="24" viewBox="0 0 30 24"><path d="M0 0h12v12L6 24H2l4-12H0zM16 0h12v12l-6 12h-4l4-12h-6z" fill="#e8232b"/></svg>
    <h5>GOOD CUSTOMER CARE</h5>
    <span class="who">Tovah</span>
    <div class="stars">
      <svg width="80" height="14" viewBox="0 0 80 14"><g fill="#e8232b"><use href="#s"/><use href="#s" x="16"/><use href="#s" x="32"/><use href="#s" x="48"/></g><use href="#s" x="64" fill="none" stroke="#e8232b"/></svg>
    </div>
    <p>Neque porro quisquam est, qui dolorem ipsum quia dolor sit amet, consectetur, adipisci velit, sed quia non numquam eius modi tempora.</p>
  </div>
</section>

<footer class="site-footer" role="img" aria-label="Faint regional map behind the footer">
  <div class="brand footer-brand" style="position:absolute;left:100px;top:160px"><span class="brand-mark"></span>Holt Rigging</div>
  <div class="footer-col" style="left:341px">
    <h6>QUICK LINKS</h6><div class="rule"></div>
    <ul class="quick-links"><li>› Home</li><li>› Services</li><li>› Gallery</li><li>› Rigging</li><li>› Testimonials</li><li>› Contact Us</li></ul>
  </div>
  <div class="footer-col" style="left:536px">
    <h6>CONTACT US</h6><div class="rule"></div>
    <div class="contact-item"><span class="ring"><svg width="14" height="18" viewBox="0 0 14 18"><path d="M7 0a7 7 0 017 7c0 5-7 11-7 11S0 12 0 7a7 7 0 017-7z" fill="#e8232b"/><circle cx="7" cy="7" r="2.5" fill="#fff"/></svg></span><div><b>ADDRESS,</b><span>45 Mason Lane, Eastford,<br>UK, 5678</span></div></div>
    <div class="contact-item"><span class="ring"><svg width="10" height="16" viewBox="0 0 10 16"><rect x="0.5" y="0.5" width="9" height="15" rx="2" fill="none" stroke="#e8232b" stroke-width="1.5"/><circle cx="5" cy="13" r="1" fill="#e8232b"/></svg></span><div><b>PHONE:</b><span>180 555 0142</span></div></div>
    <div class="contact-item"><span class="ring"><svg width="16" height="12" viewBox="0 0 16 12"><rect width="16" height="12" rx="1" fill="#e8232b"/><path d="M1 1l7 6 7-6" fill="none" stroke="#fff"/></svg></span><div><b>Mail:</b><span>info@holtrigging.com</span></div></div>
  </div>
  <div class="footer-col" style="left:813px">
    <h6>CONTACT FORM</h6><div class="rule"></div>
    <div class="contact-form">
      <div class="field" style="left:0;top:0;width:138px;height:36px">Name</div>
      <div class="field" style="left:148px;top:0;width:138px;height:36px">Phone</div>
      <div class="field" style="left:0;top:48px;width:286px;height:66px">Message</div>
    </div>
    <span class="send" style="top:226px">SEND MESSAGE</span>
  </div>
</footer>
<div class="footer-bar">
  <span class="copy">Copyright © 2017 Holt Rigging. All Rights Reserved.</span>
  <div class="footer-social"><span></span><span></span><span></span><span></span><span></span></div>
</div>

</body>
</html>
```